Packaging for Cellphone and tablet case
Need Professional Design
We need packaging for leather case for tablets and cellphones. Minimal design and content. at least 60% transparent area to make product visible from front and back.
Incorporate our logo, packaging colors, Black, grey and white.
Electronics
General audience
Must provide PSD or AI file, Resolution of 300 PPI.
LoGo AI File
This is the sample package that was designed initially,
We would like to have same amount of content on the back and front side of the package.
Sample leather.
Screen Protector packaging that we use.

```html
<!DOCTYPE html>
<html lang="en">
<head>
<meta charset="utf-8">
<title>KORVANE Case Packaging – Flat Dieline</title>
<link rel="stylesheet" href="https://fonts.googleapis.com/css2?family=Michroma&family=Roboto:wght@400;700&display=swap">
<style>
  :root {
    --stage: #e6ebf0;
    --card-black: #0d0d0e;
    --pattern-grey: #2a2b2e;
    --flap-grey: #d8d9db;
    --flap-edge: #b9bbbe;
    --window: #eef3f7;
    --window-edge: #8e959c;
    --white: #ffffff;
    --muted: #b8bcc1;
  }
  html, body {
    margin: 0;
    width: 1200px;
    height: 636px;
    overflow: hidden;
    background: var(--stage);
  }
  .dieline {
    display: block;
    width: 1200px;
    height: 636px;
  }
  .brand-name {
    font-family: "Michroma", sans-serif;
    font-size: 30px;
    letter-spacing: 4px;
    fill: var(--white);
  }
  .feature-title {
    font-family: "Roboto", sans-serif;
    font-weight: 700;
    font-size: 10px;
    fill: var(--white);
  }
  .feature-note {
    font-family: "Roboto", sans-serif;
    font-size: 7px;
    fill: var(--muted);
  }
  .model-label {
    font-family: "Roboto", sans-serif;
    font-weight: 700;
    font-size: 10px;
    fill: var(--card-black);
  }
</style>
</head>
<body>
<svg class="dieline" viewBox="0 0 1200 636" xmlns="http://www.w3.org/2000/svg">
  <!-- backing flaps -->
  <g class="backing-flaps">
    <rect x="228" y="78" width="780" height="520" rx="6" fill="var(--flap-grey)" stroke="var(--flap-edge)"/>
    <rect x="238" y="88" width="22" height="500" fill="var(--white)" opacity="0.7"/>
    <rect x="976" y="88" width="22" height="500" fill="var(--white)" opacity="0.7"/>
  </g>

  <!-- hanger tab -->
  <g class="hanger-tab">
    <rect x="560" y="28" width="120" height="70" rx="4" fill="var(--card-black)"/>
    <rect x="596" y="44" width="48" height="12" rx="6" fill="var(--stage)"/>
  </g>

  <!-- front card -->
  <path class="front-card" d="M250 92 H966 V584 H300 Q250 584 250 534 Z" fill="var(--card-black)"/>

  <!-- pattern bands -->
  <rect class="pattern-band-top" x="250" y="92" width="716" height="78" fill="var(--pattern-grey)"
        role="img" aria-label="Repeating monogram pattern band in dark grey"/>
  <rect class="pattern-band-side" x="862" y="170" width="104" height="330" fill="var(--pattern-grey)"
        role="img" aria-label="Repeating monogram pattern band in dark grey"/>

  <!-- product window -->
  <path class="product-window" d="M304 170 H840 Q856 170 856 190 V480 Q856 500 836 500 H330 Q300 500 300 470 V200 Q300 170 304 170 Z"
        fill="var(--window)" stroke="var(--window-edge)" stroke-width="2"/>

  <!-- brand -->
  <g class="brand">
    <rect x="300" y="530" width="16" height="16" fill="var(--white)"/>
    <text class="brand-name" x="326" y="548">KORVANE</text>
  </g>

  <!-- features -->
  <g class="features">
    <g class="feature">
      <rect x="690" y="516" width="14" height="16" rx="2" fill="none" stroke="var(--white)" stroke-width="1.5"/>
      <text class="feature-title" x="710" y="524">Easy Remove</text>
      <text class="feature-note" x="710" y="534">Slides out in seconds</text>
    </g>
    <g class="feature">
      <path d="M790 532 V520 Q796 512 802 520 V532" fill="none" stroke="var(--white)" stroke-width="1.5"/>
      <text class="feature-title" x="808" y="524">Easy Grip</text>
      <text class="feature-note" x="808" y="534">Soft textured finish</text>
    </g>
    <g class="feature">
      <path d="M880 532 L888 516 L896 532 Z" fill="none" stroke="var(--white)" stroke-width="1.5"/>
      <text class="feature-title" x="902" y="524">Multi Angle</text>
      <text class="feature-note" x="902" y="534">Stands two ways</text>
    </g>
  </g>

  <!-- model label -->
  <g class="model-tag">
    <rect x="860" y="550" width="96" height="24" fill="var(--white)"/>
    <text class="model-label" x="868" y="566">For Slate 2</text>
  </g>
</svg>
</body>
</html>
```